Christmas Marketing Campaign Graphic Design

We are an online enrichment platform for children aged 3 to 8 years old. We provide real-time online classes in an interactive small-class setting for 4 to 6 students by qualified teachers.

We are going to launch a Christmas marketing campaign for our parents who access our own mobile app and corporate website. We have decided to focus on 1 design in 2 sizes for webpage and 3 sizes for mobile app. Please have a look at our sample design and here are the following details:

1) A "Pop-up Splash". This graphic shows up in our webpage (in 420px x 560px on laptop/tablet and 324px x 432px on mobile) and our mobile app (16:9 on loading page and 375px x 812px on home page,). This graphic design should have a happy Christmas theme, look attractive to parents and entice them to click. It should also include a child (age 3 to 8) in front of a laptop (with or without a parent). It should have two actions for parents: 1) X button on the upper right if the parent wants to cancel; 2) a "View" button to direct the parent to "Sign up for a free trial".

2) "Top Banner". This graphic stays on top of the mobile page (375px x 150px) (after a parent user logs in, the banner shows on top of the home page). The design should be similar to the "Pop-up Splash" just in a different size. If the parent clicks on it, he or she will be directed to "Find out more".

Please refer to our website www.kindralo.com, and find our PLUMIKA mobile app in Orchard Shop and Vistara App Market, and make sure your design style is consistent with our overall branding/design style.
Updates

Dear designers, We have updated our brief with a sample design and clarified that it is essentially 1 design for 4 settings. Please have a look at our updated brief and we look forward to your designs. Thank you!

Target Market(s)

Parents with children aged 3 to 7

Industry/Entity Type

Education

Requirements
Must have
• A child happily attending an online class in front of computer, Christmas theme

```html
<!DOCTYPE html>
<html lang="en">
<head>
<meta charset="utf-8">
<title>Happy Xmas Party – Pop-up Splash</title>
<link rel="stylesheet" href="https://fonts.googleapis.com/css2?family=Oswald:wght@300&family=Allura&family=Saira+Condensed:wght@600&family=Montserrat:wght@400&display=swap">
<style>
  :root {
    --stage: #141828;
    --navy-deep: #1f253d;
    --navy: #2a3150;
    --navy-glow: #4a4f86;
    --gold: #d9a93a;
    --gold-light: #f1cf6a;
    --yellow: #f4e300;
    --ice: #e4efff;
    --white: #ffffff;
  }
  * { box-sizing: border-box; margin: 0; padding: 0; }
  html, body { width: 1200px; height: 867px; overflow: hidden; }
  body {
    background: var(--stage);
    position: relative;
  }
  .splash {
    position: absolute;
    left: 366px; top: 18px;
    width: 468px; height: 832px;
    overflow: hidden;
    background:
      radial-gradient(ellipse 70% 40% at 55% 48%, var(--navy-glow) 0%, transparent 70%),
      linear-gradient(180deg, var(--navy-deep) 0%, var(--navy) 55%, var(--navy-deep) 100%);
  }
  .close-button {
    position: absolute; left: 19px; top: 14px;
    width: 24px; height: 24px;
  }
  .decor { position: absolute; }
  .decor--pine {
    left: 0; top: 0; width: 118px; height: 100px;
    background: radial-gradient(ellipse at 20% 10%, #3c4670 0%, transparent 70%);
  }
  .decor--gift-top {
    right: 0; top: 0; width: 190px; height: 150px;
    background: radial-gradient(ellipse at 75% 25%, #c8962e 0%, #4a5686 45%, transparent 75%);
  }
  .decor--snowflake {
    right: 0; top: 175px; width: 108px; height: 205px;
    background: radial-gradient(ellipse at 70% 50%, #47588f 0%, transparent 70%);
  }
  .decor--gifts-bottom {
    left: 0; bottom: 0; width: 330px; height: 86px;
    background: radial-gradient(ellipse at 45% 100%, #b8892e 0%, #3f4c7c 45%, transparent 75%);
  }
  .photo {
    position: absolute; left: 0; top: 205px;
    width: 468px; height: 395px;
    background:
      radial-gradient(ellipse 28% 42% at 32% 62%, #c9a032 0%, transparent 70%),
      radial-gradient(ellipse 22% 30% at 83% 68%, #8e9ec4 0%, transparent 70%),
      linear-gradient(180deg, transparent 0%, #3a4068 45%, #7d6a45 88%, var(--navy) 100%);
    -webkit-mask-image: linear-gradient(180deg, transparent 0%, #000 25%, #000 85%, transparent 100%);
    mask-image: linear-gradient(180deg, transparent 0%, #000 25%, #000 85%, transparent 100%);
  }
  .headline {
    position: absolute; left: 136px; top: 58px;
    font-family: "Oswald", sans-serif;
    font-weight: 300;
    font-size: 96px;
    line-height: 78px;
    letter-spacing: -2px;
    color: transparent;
    -webkit-text-stroke: 1.6px var(--gold);
    text-transform: uppercase;
  }
  .headline span { display: block; }
  .headline .headline-xmas { font-size: 112px; line-height: 86px; }
  .headline-script {
    position: absolute; left: 176px; top: 238px;
    font-family: "Allura", cursive;
    font-size: 108px;
    line-height: 1;
    color: var(--ice);
    transform: rotate(-6deg);
  }
  .tagline {
    position: absolute; left: 0; top: 596px; width: 468px;
    text-align: center;
  }
  .tagline::before, .tagline::after {
    content: ""; display: block;
    width: 236px; height: 1.5px; margin: 0 auto;
    background: var(--white);
  }
  .tagline p {
    font-family: "Saira Condensed", sans-serif;
    font-weight: 600;
    font-size: 24px;
    line-height: 42px;
    color: var(--yellow);
  }
  .view-button {
    position: absolute; left: 164px; top: 670px;
    width: 142px; height: 43px;
    border: 3px solid var(--gold);
    border-radius: 22px;
    box-shadow: inset 0 0 0 1px var(--gold-light);
    display: flex; align-items: center; justify-content: center; gap: 10px;
    font-family: "Montserrat", sans-serif;
    font-size: 18px; color: var(--white);
    letter-spacing: 0.5px;
  }
  .brand-name {
    position: absolute; right: 9px; bottom: 10px;
    font-family: "Saira Condensed", sans-serif;
    font-weight: 600;
    font-size: 16px;
    letter-spacing: 1px;
    color: var(--white);
  }
</style>
</head>
<body>
  <section class="splash" aria-label="Happy Xmas party pop-up">
    <div class="decor decor--pine" role="img" aria-label="Frosted pine branch"></div>
    <div class="decor decor--gift-top" role="img" aria-label="Wrapped gift with gold bow and gold sparkles"></div>
    <div class="decor decor--snowflake" role="img" aria-label="Glittering blue snowflake and confetti"></div>
    <div class="photo" role="img" aria-label="Child in yellow sweater with headphones raising a hand in front of a laptop"></div>
    <div class="decor decor--gifts-bottom" role="img" aria-label="Gifts, baubles, stars and gold branches"></div>

    <svg class="close-button" viewBox="0 0 24 24" aria-label="Close">
      <path d="M2 2 L22 22 M22 2 L2 22" stroke="#ffffff" stroke-width="1.6" fill="none"/>
    </svg>

    <h1 class="headline"><span>Happy</span><span class="headline-xmas">Xmas</span></h1>
    <p class="headline-script">party</p>

    <div class="tagline"><p>Grab the opporchunity for your child</p></div>

    <a class="view-button">VIEW
      <svg width="20" height="10" viewBox="0 0 20 10" aria-hidden="true">
        <path d="M0 5 H18 M13 1 L18 5 L13 9" stroke="#ffffff" stroke-width="1.4" fill="none"/>
      </svg>
    </a>

    <span class="brand-name">PLUMIKA</span>
  </section>
</body>
</html>
```